Folder & Business Card for Automation Company
Brightwell Torque Mfr.
Folder & Business Card for Automation Company - Manufacturing
Creative Brief
Professional
Darren Okafor
Vice President
4817 Halvern Road Merriam, KS 66209
do@brightwelltorquemfr.example
www.brightwelltorquemfr.example
Along with a business card we are looking for a design for the front cover of a folder to be used for sales literature. The cover should also include our logo.

```html
<!DOCTYPE html>
<html lang="en">
<head>
<meta charset="utf-8">
<title>Brightwell Torque Mfr. – Business Card</title>
<link rel="stylesheet" href="https://fonts.googleapis.com/css2?family=Cinzel:wght@400;700&display=swap">
<style>
  :root {
    --backdrop: #e4e2df;
    --card-white: #ffffff;
    --card-mist: #eef0f1;
    --charcoal: #2d2e30;
    --charcoal-deep: #1f2022;
    --signal-red: #d3232f;
    --ink: #26272a;
    --text-light: #f1f1f1;
    --text-soft: #c9cacc;
  }
  * { margin: 0; padding: 0; box-sizing: border-box; }
  html, body {
    width: 1200px;
    height: 914px;
    overflow: hidden;
    background: var(--backdrop);
  }
  .business-card {
    position: absolute;
    left: 75px;
    top: 157px;
    width: 1050px;
    height: 600px;
    background: linear-gradient(180deg, var(--card-white) 0%, var(--card-mist) 45%);
    overflow: hidden;
    box-shadow: 0 10px 30px rgba(0,0,0,0.18);
    font-family: "Cinzel", serif;
  }
  .card-waves {
    position: absolute;
    inset: 0;
    width: 100%;
    height: 100%;
  }
  .brand {
    position: absolute;
    top: 130px;
    left: 0;
    width: 100%;
    display: flex;
    justify-content: center;
    align-items: center;
    gap: 18px;
  }
  .brand-dot {
    width: 34px;
    height: 34px;
    border-radius: 50%;
    background: var(--signal-red);
  }
  .brand-name {
    font-family: "Cinzel", serif;
    font-weight: 700;
    font-size: 44px;
    letter-spacing: 1px;
    color: var(--ink);
  }
  .contact-person {
    position: absolute;
    right: 540px;
    top: 368px;
    text-align: right;
    color: var(--text-light);
  }
  .person-name {
    font-size: 27px;
    font-weight: 400;
    letter-spacing: 1px;
  }
  .person-title {
    font-size: 21px;
    color: var(--text-soft);
    margin-top: 2px;
  }
  .person-address {
    margin-top: 22px;
    font-size: 20px;
    line-height: 30px;
    color: var(--text-soft);
  }
  .divider {
    position: absolute;
    left: 532px;
    top: 372px;
    width: 2px;
    height: 170px;
    background: var(--text-soft);
  }
  .contact-lines {
    position: absolute;
    left: 552px;
    top: 372px;
    list-style: none;
    color: var(--text-soft);
    font-size: 18px;
  }
  .contact-lines li {
    display: flex;
    align-items: center;
    gap: 12px;
    height: 42px;
  }
  .contact-icon {
    width: 24px;
    height: 24px;
    flex: none;
  }
</style>
</head>
<body>
  <div class="business-card">
    <svg class="card-waves" viewBox="0 0 1050 600" preserveAspectRatio="none" aria-hidden="true">
      <path d="M0,255 C300,205 650,290 1050,160 L1050,196 C650,318 300,238 0,288 Z" fill="var(--signal-red)"/>
      <path d="M0,288 C300,238 650,318 1050,196 L1050,214 C650,338 300,262 0,306 Z" fill="#d8dadc"/>
      <path d="M0,306 C300,262 650,338 1050,214 L1050,600 L0,600 Z" fill="var(--charcoal)"/>
      <path d="M0,520 C350,500 700,560 1050,520 L1050,600 L0,600 Z" fill="var(--charcoal-deep)" opacity="0.6"/>
    </svg>

    <div class="brand">
      <span class="brand-dot"></span>
      <span class="brand-name">Brightwell Torque Mfr.</span>
    </div>

    <div class="contact-person">
      <p class="person-name">Darren Okafor</p>
      <p class="person-title">Vice President</p>
      <p class="person-address">4817 Halvern Road<br>Ashbury, NE 68901</p>
    </div>

    <div class="divider"></div>

    <ul class="contact-lines">
      <li>
        <svg class="contact-icon" viewBox="0 0 24 24"><circle cx="12" cy="12" r="11" fill="var(--text-soft)"/><path d="M8.5 6.5l2 2.5-1.2 1.3c.7 1.6 2 2.9 3.4 3.6l1.3-1.2 2.5 2-1.3 2c-4.5-.5-8.1-4.2-8.6-8.6z" fill="var(--charcoal)"/></svg>
        <span>555-201-0142</span>
      </li>
      <li>
        <svg class="contact-icon" viewBox="0 0 24 24"><circle cx="12" cy="12" r="11" fill="var(--text-soft)"/><rect x="8" y="6" width="8" height="4" fill="var(--charcoal)"/><rect x="6" y="10" width="12" height="5" rx="1" fill="var(--charcoal)"/><rect x="8" y="14" width="8" height="4" fill="var(--charcoal)"/></svg>
        <span>555-201-0178</span>
      </li>
      <li>
        <svg class="contact-icon" viewBox="0 0 24 24"><circle cx="12" cy="12" r="11" fill="var(--text-soft)"/><rect x="6" y="8" width="12" height="8" fill="var(--charcoal)"/><path d="M6 8l6 4.5L18 8" stroke="var(--text-soft)" stroke-width="1.2" fill="none"/></svg>
        <span>do@brightwelltorquemfr.example</span>
      </li>
      <li>
        <svg class="contact-icon" viewBox="0 0 24 24"><circle cx="12" cy="12" r="11" fill="var(--text-soft)"/><circle cx="12" cy="12" r="6" fill="none" stroke="var(--charcoal)" stroke-width="1.4"/><ellipse cx="12" cy="12" rx="2.6" ry="6" fill="none" stroke="var(--charcoal)" stroke-width="1.2"/><path d="M6 12h12" stroke="var(--charcoal)" stroke-width="1.2"/></svg>
        <span>www.brightwelltorquemfr.example</span>
      </li>
    </ul>
  </div>
</body>
</html>
```